Business card design needed

I need a business card for a new company based in Perth, Western Australia, called KT Power Pty Ltd.

I'm the sole proprietor, and have 25 years' experience in directorship, senior commercial/business development/strategy roles in the oil & gas industry with both supermajors and junior listed companies. I also have interests in renewable energy (and am co-founder and director of a separate renewable energy start-up company). KT Power will be the vehicle for me to contract my services, principally in the oil & gas industry (although this will include directorship services to the renewable energy company). These services will include general consultancy in my areas of expertise, and contracting to provide senior management/director services to start-up or junior oil and gas companies.

I'm looking for a design that communicates professionalism, dynamism, experience, strategic skills and growth.

My Proflinker profile may also be useful context;

"I have a real passion for discovering new investment opportunities and turning them from talk into reality. Right now my focus is on oil, gas and energy ventures. I’m always on the look out for compelling new investment opportunities where I can bring my leadership and strategic insight to bear to make a real difference by delivering transformational results.

I spent 24 years with NX where I built up extensive international experience in oil, gas and energy and was a member of the company’s “fast track” development programme. As an entrepreneurial senior commercial leader, strategic thinker and tactical dealmaker I was responsible for numerous deals such as divestments, farm-ins, asset swaps, new acreage bids, unitizations, gas and LNG sales, creating billions of dollars of value for NX. These deals frequently broke new ground and/or required an innovative approach that delivered results in excess of what the business thought achievable. I have held senior executive and director roles covering Exploration & Production, Mergers & Acquisitions, Business Development, LNG Marketing, Joint Venture Management, Gas & Power and Corporate head office. International assignments included UK, Australia, Indonesia, Norway & Belgium.

I’m a member of the Guild of Global Fuel Brokers (GGFB) and the National Council of Board Officers (NCBO).

Board experience comprises four directorships and two alternate directorships of Australian companies, and directorship of a Not for Profit organisation.

Specialties
Strategy, Business Development, Mergers & Acquisitions, Joint Venture Management, Negotiation, Gas & LNG Marketing."

Target Market(s)

Oil and gas or energy companies of all sizes from large listed companies to start-ups - also service providers to the industry.

Industry/Entity Type

Oil And Gas

Contact Information for Business Card

KT Power Pty Ltd
Martin Dacombe
27C Ferncliff Road,
Holloway Vale,
WA 6999

Tel +61 400 555 817
email dacombemj@quenvol.example.au

```html
<!DOCTYPE html>
<html lang="en">
<head>
<meta charset="utf-8">
<title>KT Power Pty Ltd – Business Cards</title>
<link rel="stylesheet" href="https://fonts.googleapis.com/css2?family=Source+Sans+3:wght@400;600;700&display=swap">
<style>
  :root {
    --backdrop: #c4c4c4;
    --card: #ffffff;
    --ink: #1c1c1c;
    --ink-soft: #2a2a2a;
    --label: #ffffff;
    --card-shadow: rgba(0, 0, 0, 0.28);
  }
  * { box-sizing: border-box; margin: 0; padding: 0; }
  html, body {
    width: 1200px;
    height: 913px;
    overflow: hidden;
  }
  body {
    position: relative;
    background: var(--backdrop);
    font-family: "Source Sans 3", "Myriad Pro", Arial, sans-serif;
    color: var(--ink);
  }
  .card {
    position: absolute;
    width: 478px;
    height: 278px;
    background: var(--card);
    box-shadow: 2px 3px 5px var(--card-shadow);
  }
  .card--one-sided { left: 78px; top: 294px; }
  .card--front { left: 652px; top: 162px; }
  .card--back { left: 646px; top: 466px; }

  .contact {
    position: absolute;
    font-size: 15px;
    line-height: 18px;
    color: var(--ink-soft);
    font-weight: 400;
  }
  .card--one-sided .contact { left: 20px; top: 16px; }
  .card--front .contact { left: 22px; top: 33px; }

  .identity { position: absolute; }
  .card--one-sided .identity { left: 21px; top: 84px; }
  .card--front .identity { left: 22px; top: 139px; }
  .company {
    font-size: 15px;
    font-weight: 700;
    line-height: 18px;
  }
  .person {
    font-size: 28px;
    font-weight: 700;
    line-height: 32px;
    letter-spacing: -0.2px;
  }

  .services {
    position: absolute;
    list-style: none;
    font-size: 15.5px;
    line-height: 20px;
  }
  .card--one-sided .services { left: 22px; top: 146px; font-weight: 400; }
  .card--back .services { left: 23px; top: 74px; font-weight: 700; }

  .brand {
    position: absolute;
    display: flex;
    align-items: center;
    gap: 7px;
    font-weight: 700;
    color: var(--ink);
    white-space: nowrap;
  }
  .brand__dot {
    display: block;
    border-radius: 50%;
    background: var(--ink);
  }
  .card--one-sided .brand { left: 292px; top: 125px; font-size: 20px; }
  .card--one-sided .brand__dot { width: 22px; height: 22px; }
  .card--front .brand { left: 293px; top: 128px; font-size: 19px; }
  .card--front .brand__dot { width: 20px; height: 20px; }
  .card--back .brand { left: 320px; top: 125px; font-size: 13px; gap: 5px; }
  .card--back .brand__dot { width: 12px; height: 12px; }

  .caption {
    position: absolute;
    color: var(--label);
    font-size: 26px;
    font-weight: 700;
    letter-spacing: 0.2px;
  }
  .caption--one-sided { left: 90px; top: 602px; }
  .caption--two-sided { left: 886px; top: 786px; }
</style>
</head>
<body>

  <article class="card card--one-sided" aria-label="One-sided business card">
    <address class="contact" style="font-style:normal">
      27C Ferncliff Road, Holloway Vale, WA 6999<br>
      Tel +61 400 555 817<br>
      email dacombemj@quenvol.example.au
    </address>
    <div class="identity">
      <p class="company">KT Power Pty Ltd</p>
      <p class="person">Martin Dacombe</p>
    </div>
    <ul class="services">
      <li>Strategy</li>
      <li>Negotiation</li>
      <li>Gas &amp; LNG Marketing</li>
      <li>Business Development</li>
      <li>Mergers &amp; Acquisitions</li>
      <li>Joint Venture Management</li>
    </ul>
    <div class="brand"><span class="brand__dot"></span>KT Power</div>
  </article>

  <article class="card card--front" aria-label="Two-sided business card, front">
    <address class="contact" style="font-style:normal">
      27C Ferncliff Road, Holloway Vale, WA 6999<br>
      Tel +61 400 555 817<br>
      email dacombemj@quenvol.example.au
    </address>
    <div class="identity">
      <p class="company">KT Power Pty Ltd</p>
      <p class="person">Martin Dacombe</p>
    </div>
    <div class="brand"><span class="brand__dot"></span>KT Power</div>
  </article>

  <article class="card card--back" aria-label="Two-sided business card, back">
    <ul class="services">
      <li>Strategy</li>
      <li>Negotiation</li>
      <li>Gas &amp; LNG Marketing</li>
      <li>Business Development</li>
      <li>Mergers &amp; Acquisitions</li>
      <li>Joint Venture Management</li>
    </ul>
    <div class="brand"><span class="brand__dot"></span>KT Power</div>
  </article>

  <p class="caption caption--one-sided">one-sided card</p>
  <p class="caption caption--two-sided">two-sided card</p>

</body>
</html>
```